"Pillowtide Chews" is the brand name for CBN infused Gummies for a restful sleep

Need a label for the glass jar and a round label for the lid. The gummy shapes are crescent white mons and blue stars or gummy sheep

You can use an 6 or 8 oz clear jar. Your illustration program should have this mock up.

Font styles to use
Sans Serif

```html
<!DOCTYPE html>
<html lang="en">
<head>
<meta charset="utf-8">
<title>Pillowtide Chews – Jar and Lid Labels</title>
<link href="https://fonts.googleapis.com/css2?family=Dosis:wght@400;500;600&display=swap" rel="stylesheet">
<style>
  :root {
    --page: #ffffff;
    --night-top: #07070f;
    --night-mid: #14143a;
    --night-bottom: #1c1b55;
    --haze: rgba(200, 200, 210, 0.22);
    --amber: #f6a531;
    --rule-blue: #2e6390;
    --ink-light: #e4e4ee;
    --cell-line: #c9c9d6;
  }
  * { box-sizing: border-box; margin: 0; padding: 0; }
  html, body {
    width: 1200px;
    height: 1170px;
    overflow: hidden;
    background: var(--page);
    font-family: "Dosis", "Trebuchet MS", sans-serif;
  }
  .canvas {
    position: relative;
    width: 1200px;
    height: 1170px;
  }

  /* shared label surface */
  .night-sky {
    position: absolute;
    inset: 0;
    background:
      radial-gradient(ellipse 38% 14% at 50% 17%, var(--haze), transparent 70%),
      linear-gradient(180deg, var(--night-top) 0%, var(--night-mid) 55%, var(--night-bottom) 100%);
  }
  .label-content {
    position: relative;
    display: flex;
    flex-direction: column;
    align-items: center;
    color: var(--ink-light);
  }
  .brand-name {
    color: var(--amber);
    font-weight: 500;
    line-height: 1;
    letter-spacing: 0.5px;
    white-space: nowrap;
  }
  .brand-rule {
    background: var(--rule-blue);
    border-radius: 3px;
  }
  .product-line {
    color: var(--amber);
    font-weight: 500;
    letter-spacing: 0.5px;
    text-transform: uppercase;
    line-height: 1.2;
  }
  .seal-mark {
    flex: none;
    border: 2px solid var(--amber);
    border-radius: 50%;
    opacity: 0.85;
  }

  /* jar wrap label */
  .jar-label {
    position: absolute;
    left: 100px;
    top: 70px;
    width: 1000px;
    height: 575px;
    overflow: hidden;
  }
  .jar-label .label-content { padding-top: 150px; }
  .jar-label .brand-name { font-size: 80px; }
  .jar-label .brand-rule { width: 540px; height: 7px; margin-top: 10px; }
  .jar-label .product-line { font-size: 26px; margin-top: 6px; }

  .fact-table {
    display: flex;
    margin-top: 44px;
    border: 1.5px solid var(--cell-line);
  }
  .fact-cell {
    width: 156px;
    height: 78px;
    display: flex;
    flex-direction: column;
    align-items: center;
    justify-content: center;
    text-transform: uppercase;
    font-size: 21px;
    letter-spacing: 1.5px;
    line-height: 1.15;
    text-align: center;
  }
  .fact-cell + .fact-cell { border-left: 1.5px solid var(--cell-line); }
  .fact-cell .fact-figure { font-size: 32px; letter-spacing: 1px; }
  .flavor-note {
    margin-top: 12px;
    font-size: 21px;
    letter-spacing: 2px;
    line-height: 1.2;
    text-transform: uppercase;
  }
  .jar-label .seal-mark { width: 54px; height: 54px; margin-top: 26px; }

  /* lid label */
  .lid-label {
    position: absolute;
    left: 380px;
    top: 690px;
    width: 440px;
    height: 440px;
    border-radius: 50%;
    overflow: hidden;
  }
  .lid-label .label-content { padding-top: 168px; }
  .lid-label .brand-name { font-size: 50px; }
  .lid-label .brand-rule { width: 330px; height: 5px; margin-top: 8px; }
  .lid-label .product-line { font-size: 19px; margin-top: 5px; }
  .lid-label .seal-mark { width: 50px; height: 50px; margin-top: 58px; }
</style>
</head>
<body>
<main class="canvas">

  <section class="jar-label" aria-label="Jar wrap label">
    <div class="night-sky" role="img" aria-label="Starry night sky with a glowing crescent moon and soft cloud"></div>
    <div class="label-content">
      <h1 class="brand-name">Pillowtide Chews</h1>
      <div class="brand-rule"></div>
      <p class="product-line">Gummies infused with CBN</p>
      <div class="fact-table">
        <div class="fact-cell"><span class="fact-figure">30</span><span>Gummies</span></div>
        <div class="fact-cell"><span>Sleep</span><span>Relief</span></div>
        <div class="fact-cell"><span>20mg CBN</span><span>/Package</span></div>
      </div>
      <p class="flavor-note">Natural Flavored</p>
      <div class="seal-mark" aria-hidden="true"></div>
    </div>
  </section>

  <section class="lid-label" aria-label="Round lid label">
    <div class="night-sky" role="img" aria-label="Starry night sky with a glowing crescent moon and soft cloud"></div>
    <div class="label-content">
      <h2 class="brand-name">Pillowtide Chews</h2>
      <div class="brand-rule"></div>
      <p class="product-line">Gummies infused with CBN</p>
      <div class="seal-mark" aria-hidden="true"></div>
    </div>
  </section>

</main>
</body>
</html>
```